Murder Mystery Buffet Dinner Fundraiser. An Evening of Murder, Mystery & Mayhem

Camp fundraiser needs a 7-element promotional package. The elements are 1) a save the date post card, 2) a two-sided invitation, 3) an invitation envelope, 4) a rsvp card, 5) a rsvp envelope, 6) the front page of a playbill size program book and 7) a 8.5" x 11" flyer. We hope to attract 125 donors to attend a fundraising murder mystery buffet dinner to support a 70 + year old residential summer camp. We would like the elements in the package to be consist with one another. The package should have a consistent theme. The theme should be mysterious, but playful and engaging.

Target Market(s)

middle class, 25 to 70 year olds

Other font styles liked:
• Broadway Playbill style

Colors

Designer to choose colors to be used in the design.

Requirements
Must have
• A mysterious, fun off Broadway feeling
Nice to have
• Perhaps a shadowy mysterious figure(s) or 5 playing cards, 10, jack, queen , king, ace, either individually or collectively, representing something sinister
Should not have
• Anything above a pg rating

```html
<!DOCTYPE html>
<html lang="en">
<head>
<meta charset="utf-8">
<title>Alder Camp and Retreat Center – Save the Date</title>
<link href="https://fonts.googleapis.com/css2?family=Barlow:wght@300;400;500&display=swap" rel="stylesheet">
<style>
  :root {
    --paper: #ffffff;
    --ink: #111111;
    --forest: #3a6b3f;
    --lake: #2f7080;
  }
  html, body {
    margin: 0;
    padding: 0;
    overflow: hidden;
    background: var(--paper);
  }
  .postcard {
    position: relative;
    width: 851px;
    height: 1200px;
    background: var(--paper);
    color: var(--ink);
    font-family: "Barlow", sans-serif;
    overflow: hidden;
  }
  .brand {
    position: absolute;
    top: 58px;
    left: 0;
    width: 100%;
    display: flex;
    justify-content: center;
    align-items: center;
    gap: 14px;
  }
  .brand-dot {
    width: 46px;
    height: 46px;
    border-radius: 50%;
    background: var(--forest);
  }
  .brand-name {
    font-size: 34px;
    font-weight: 500;
    letter-spacing: 2px;
    color: var(--forest);
  }
  .org-name {
    position: absolute;
    top: 150px;
    left: 0;
    width: 100%;
    text-align: center;
    font-size: 22px;
    font-weight: 500;
    letter-spacing: 0.3px;
    margin: 0;
  }
  .headline {
    position: absolute;
    top: 305px;
    left: 0;
    width: 100%;
    margin: 0;
    text-align: center;
    font-size: 63px;
    font-weight: 400;
    line-height: 73px;
    letter-spacing: 0.5px;
  }
  .write-lines {
    position: absolute;
    left: 156px;
    top: 703px;
    width: 539px;
    margin: 0;
    padding: 0;
    list-style: none;
  }
  .write-lines li {
    height: 52px;
    border-top: 1.6px solid var(--ink);
  }
  .stamp-box {
    position: absolute;
    left: 639px;
    top: 950px;
    width: 144px;
    height: 195px;
    border: 3.5px solid var(--ink);
    display: flex;
    align-items: center;
    justify-content: center;
  }
  .stamp-label {
    font-size: 31px;
    font-weight: 300;
    letter-spacing: 1px;
    transform: rotate(-35deg);
  }
</style>
</head>
<body>
  <main class="postcard">
    <div class="brand">
      <span class="brand-dot"></span>
      <span class="brand-name">ALDER</span>
    </div>
    <p class="org-name">ALDER CAMP AND RETREAT CENTER</p>
    <h1 class="headline">JOIN US FOR<br>AN EVENING OF<br>MYSTERY, MAYHEM<br>AND MURDER!</h1>
    <ul class="write-lines">
      <li></li><li></li><li></li><li></li>
    </ul>
    <div class="stamp-box"><span class="stamp-label">STAMP</span></div>
  </main>
</body>
</html>
```